Re-style home page - eye-catching and unique design for social commerce website

We need a new concept design for Trondix's home page.
We don't want to make huge changes but creating a more professional and eye-catching style.

We need to look very serious like a professional services company and in the same time to look like a social network for e-commerce.

Our logo is very captive and you can use to creating something of harmonious.

This is a re-style and I'm excepted to see unique and fresh design like Glimmora.
Updates

Target Market(s)

e-commerce and social

Industry/Entity Type

Social

Number of Pages Required

1 page

Font styles to use
Serif
Sans Serif

Requirements
Must have
• An eye-catching result.
• Search bar with logo and Login How it works and business
• The slogan with login and signup.
• Footer links.
Nice to have
• I would like to open the home page and see only two clear ways:
• -Consumer
• --Search
• --The slogan
• --Login and Signup
• --How it works
• -Business
• --Go to Business area
• Background: City, Shopping.
Should not have
• Scrollbar style!

```html
<!DOCTYPE html>
<html lang="en">
<head>
<meta charset="utf-8">
<title>Trondix – Home</title>
<link href="https://fonts.googleapis.com/css2?family=Open+Sans:wght@400;600;700&family=Roboto:wght@400;500;700&display=swap" rel="stylesheet">
<style>
  :root {
    --navy: #26255c;
    --navy-deep: #22215a;
    --coral: #ff5346;
    --coral-light: #ff6a52;
    --red-line: #e5423a;
    --search-red: #e8423f;
    --linkora-blue: #2c4a8c;
    --page-bg: #22262d;
    --card-bg: #2f343c;
    --card-text: #c9ccd1;
    --heart: #e0483e;
    --white: #ffffff;
    --field-bg: #f2f2f2;
    --field-text: #3a3a3a;
  }
  * { box-sizing: border-box; margin: 0; padding: 0; }
  html, body { width: 1200px; height: 911px; overflow: hidden; }
  body {
    position: relative;
    background: var(--page-bg);
    font-family: "Open Sans", Arial, sans-serif;
  }

  /* Feed in the background */
  .feed {
    position: absolute;
    left: 22px; top: 60px;
    display: grid;
    grid-template-columns: repeat(4, 308px);
    grid-template-rows: 253px 260px 260px 260px;
    column-gap: 24px;
    row-gap: 24px;
    filter: blur(1.6px);
  }
  .post { background: var(--card-bg); align-self: start; padding: 0 8px 16px; }
  .post-media { height: 188px; }
  .post-info {
    display: flex; justify-content: space-between; align-items: flex-start;
    padding: 18px 14px 0;
  }
  .post-title {
    width: 140px;
    font-family: "Roboto", Arial, sans-serif;
    font-size: 11px; font-weight: 700; line-height: 15px;
    color: var(--card-text); text-transform: uppercase; letter-spacing: 0.2px;
  }
  .post-stats { display: flex; gap: 10px; font-size: 11px; color: var(--card-text); }
  .stat { display: flex; align-items: center; gap: 4px; }
  .stat-likes { color: var(--heart); }
  .feed-shade { position: absolute; inset: 0; background: rgba(20, 22, 28, 0.18); }

  /* Header */
  .site-header {
    position: absolute; left: 0; top: 0; width: 1200px; height: 89px;
    background: var(--navy);
    border-bottom: 1px solid var(--red-line);
  }
  .brand {
    position: absolute; left: 100px; top: 24px;
    display: flex; align-items: center; gap: 8px;
    font-family: "Open Sans", Arial, sans-serif;
    font-weight: 700; font-size: 34px; letter-spacing: -1px; color: var(--white);
  }
  .brand-square { width: 26px; height: 26px; background: var(--coral); }
  .search {
    position: absolute; left: 316px; top: 27px; width: 470px; height: 39px;
    background: var(--white); border-radius: 3px; padding: 3px;
  }
  .search-button {
    position: absolute; right: 3px; top: 3px; width: 103px; height: 33px;
    background: linear-gradient(#ef4d45, var(--search-red));
    border: none; border-radius: 3px;
    color: var(--white); font-family: "Open Sans", Arial, sans-serif;
    font-weight: 700; font-size: 14px; letter-spacing: 0.5px;
  }
  .main-nav a {
    position: absolute; top: 38px;
    font-family: "Roboto", Arial, sans-serif; font-size: 14px;
    color: var(--white); text-decoration: none;
  }

  /* Login panel */
  .login-panel {
    position: absolute; left: 317px; top: 178px; width: 566px; height: 557px;
    background: linear-gradient(135deg, var(--coral-light) 0%, var(--coral) 50%, #ff4a40 100%);
    border-radius: 3px;
    color: var(--white);
  }
  .panel-tag {
    position: absolute; right: 20px; top: 16px;
    font-family: "Roboto", Arial, sans-serif; font-weight: 700; font-size: 14px;
  }
  .panel-brand {
    position: absolute; left: 0; width: 100%; top: 88px;
    display: flex; justify-content: center; align-items: center; gap: 8px;
    font-weight: 700; font-size: 28px; letter-spacing: -0.5px;
  }
  .panel-brand-square { width: 20px; height: 20px; background: var(--navy); }
  .social-login {
    position: absolute; left: 156px; top: 159px; width: 285px; height: 51px;
    background: var(--linkora-blue); border-radius: 2px;
    display: flex; align-items: center; justify-content: center; gap: 18px;
    font-family: "Roboto", Arial, sans-serif; font-size: 21px;
  }
  .social-square { width: 12px; height: 12px; background: var(--white); }
  .divider {
    position: absolute; left: 66px; top: 232px; width: 438px; height: 22px;
    display: flex; align-items: center; gap: 12px;
    font-family: "Roboto", Arial, sans-serif; font-size: 21px;
  }
  .divider::before, .divider::after {
    content: ""; flex: 1; height: 1px; background: rgba(255, 255, 255, 0.35);
  }
  .slogan {
    position: absolute; left: 0; width: 100%; top: 270px; text-align: center;
    font-weight: 600; font-size: 33px; letter-spacing: -1px;
    text-shadow: 0 2px 3px rgba(120, 20, 10, 0.45);
  }
  .field {
    position: absolute; left: 138px; width: 315px; height: 41px;
    background: var(--field-bg); border: 1px solid #e6e0de; border-radius: 3px;
    padding: 0 12px; font-family: "Open Sans", Arial, sans-serif;
    font-weight: 600; font-size: 14px; color: var(--field-text);
    display: flex; align-items: center;
  }
  .field-username { top: 336px; }
  .field-password { top: 399px; }
  .signup-button {
    position: absolute; left: 314px; top: 464px; width: 138px; height: 40px;
    background: var(--navy-deep); border: none; border-radius: 2px;
    color: var(--white); font-family: "Open Sans", Arial, sans-serif;
    font-weight: 600; font-size: 20px;
  }
</style>
</head>
<body>

<main class="feed" aria-hidden="true">
  <article class="post">
    <div class="post-media" role="img" aria-label="Dreamcatcher with feathers on a light wall" style="background:linear-gradient(135deg,#e9e2c6,#cfc49c)"></div>
    <div class="post-info"><p class="post-title">Fullscreen post with info</p><div class="post-stats"><span class="stat"><svg width="11" height="7" viewBox="0 0 11 7"><ellipse cx="5.5" cy="3.5" rx="5.5" ry="3.5" fill="#c9ccd1"/></svg>9526</span><span class="stat stat-likes"><svg width="11" height="10" viewBox="0 0 11 10"><path d="M5.5 9.5 1 5A2.6 2.6 0 0 1 5.5 1.4 2.6 2.6 0 0 1 10 5Z" fill="none" stroke="#e0483e" stroke-width="1.4"/></svg>114</span></div></div>
  </article>
  <article class="post">
    <div class="post-media" role="img" aria-label="Man in a suit crossing a grey street" style="background:linear-gradient(135deg,#b5b7b6,#8f9190)"></div>
    <div class="post-info"><p class="post-title">Post with slider gallery</p><div class="post-stats"><span class="stat">4170</span><span class="stat stat-likes">31</span></div></div>
  </article>
  <article class="post">
    <div class="post-media" role="img" aria-label="Bicycle against a white wall" style="background:linear-gradient(135deg,#f1f0ec,#d6d3cc)"></div>
    <div class="post-info"><p class="post-title">Post with video</p><div class="post-stats"><span class="stat"><svg width="11" height="7" viewBox="0 0 11 7"><ellipse cx="5.5" cy="3.5" rx="5.5" ry="3.5" fill="#c9ccd1"/></svg>6254</span><span class="stat stat-likes"><svg width="11" height="10" viewBox="0 0 11 10"><path d="M5.5 9.5 1 5A2.6 2.6 0 0 1 5.5 1.4 2.6 2.6 0 0 1 10 5Z" fill="none" stroke="#e0483e" stroke-width="1.4"/></svg>137</span></div></div>
  </article>
  <article class="post">
    <div class="post-media" role="img" aria-label="Fashion portrait in soft light" style="background:linear-gradient(135deg,#e8e4e0,#a59a92)"></div>
    <div class="post-info"><p class="post-title">Fullscreen ribbon post</p></div>
  </article>

  <article class="post">
    <div class="post-media" role="img" aria-label="Sea waves breaking on dark rocks" style="background:linear-gradient(180deg,#3f5565,#8fa2ad 60%,#2f3438)"></div>
    <div class="post-info"><p class="post-title">Video post with info</p><div class="post-stats"><span class="stat"><svg width="11" height="7" viewBox="0 0 11 7"><ellipse cx="5.5" cy="3.5" rx="5.5" ry="3.5" fill="#c9ccd1"/></svg>3152</span><span class="stat stat-likes"><svg width="11" height="10" viewBox="0 0 11 10"><path d="M5.5 9.5 1 5A2.6 2.6 0 0 1 5.5 1.4 2.6 2.6 0 0 1 10 5Z" fill="none" stroke="#e0483e" stroke-width="1.4"/></svg>24</span></div></div>
  </article>
  <article class="post">
    <div class="post-media" role="img" aria-label="Outdoor scene" style="background:linear-gradient(135deg,#6d7a80,#3c4347)"></div>
    <div class="post-info"><p class="post-title">Standard post</p></div>
  </article>
  <article class="post">
    <div class="post-media" role="img" aria-label="Colourful old town street with laundry" style="background:linear-gradient(135deg,#d98a52,#7c4b3d 60%,#4a4f5a)"></div>
    <div class="post-info"><p class="post-title">Post with map</p><div class="post-stats"><span class="stat"><svg width="11" height="7" viewBox="0 0 11 7"><ellipse cx="5.5" cy="3.5" rx="5.5" ry="3.5" fill="#c9ccd1"/></svg>6713</span><span class="stat stat-likes"><svg width="11" height="10" viewBox="0 0 11 10"><path d="M5.5 9.5 1 5A2.6 2.6 0 0 1 5.5 1.4 2.6 2.6 0 0 1 10 5Z" fill="none" stroke="#e0483e" stroke-width="1.4"/></svg>40</span></div></div>
  </article>
  <article class="post">
    <div class="post-media" role="img" aria-label="Portrait with light flowing hair" style="background:linear-gradient(135deg,#eef0f2,#c7ccd1)"></div>
    <div class="post-info"><p class="post-title">Simple post with sidebar</p></div>
  </article>

  <article class="post">
    <div class="post-media" role="img" aria-label="Close-up of a record player tonearm" style="background:linear-gradient(180deg,#3b4146,#cfd3d6 55%,#6c7378)"></div>
    <div class="post-info"><p class="post-title">Ribbon post with info</p><div class="post-stats"><span class="stat"><svg width="11" height="7" viewBox="0 0 11 7"><ellipse cx="5.5" cy="3.5" rx="5.5" ry="3.5" fill="#c9ccd1"/></svg>2895</span><span class="stat stat-likes"><svg width="11" height="10" viewBox="0 0 11 10"><path d="M5.5 9.5 1 5A2.6 2.6 0 0 1 5.5 1.4 2.6 2.6 0 0 1 10 5Z" fill="none" stroke="#e0483e" stroke-width="1.4"/></svg>17</span></div></div>
  </article>
  <article class="post">
    <div class="post-media" role="img" aria-label="Dark rock in white surf" style="background:linear-gradient(135deg,#dfe6e8,#9aa5a8)"></div>
    <div class="post-info"><p class="post-title">Post with before/after</p><div class="post-stats"><span class="stat"><svg width="11" height="7" viewBox="0 0 11 7"><ellipse cx="5.5" cy="3.5" rx="5.5" ry="3.5" fill="#c9ccd1"/></svg>2399</span><span class="stat stat-likes"><svg width="11" height="10" viewBox="0 0 11 10"><path d="M5.5 9.5 1 5A2.6 2.6 0 0 1 5.5 1.4 2.6 2.6 0 0 1 10 5Z" fill="none" stroke="#e0483e" stroke-width="1.4"/></svg>22</span></div></div>
  </article>
  <article class="post">
    <div class="post-media" role="img" aria-label="Woman in a white dress by a white door" style="background:linear-gradient(135deg,#f4f3f0,#d9d2cb)"></div>
    <div class="post-info"><p class="post-title">Post with left sidebar</p><div class="post-stats"><span class="stat"><svg width="11" height="7" viewBox="0 0 11 7"><ellipse cx="5.5" cy="3.5" rx="5.5" ry="3.5" fill="#c9ccd1"/></svg>1452</span><span class="stat stat-likes"><svg width="11" height="10" viewBox="0 0 11 10"><path d="M5.5 9.5 1 5A2.6 2.6 0 0 1 5.5 1.4 2.6 2.6 0 0 1 10 5Z" fill="none" stroke="#e0483e" stroke-width="1.4"/></svg>16</span></div></div>
  </article>
  <article class="post">
    <div class="post-media" role="img" aria-label="Fork in dark dramatic light" style="background:linear-gradient(135deg,#5a6166,#15181b)"></div>
    <div class="post-info"><p class="post-title">Simple fullwidth video post</p></div>
  </article>

  <article class="post"><div class="post-media" style="background:#3a3f47"></div></article>
  <article class="post"><div class="post-media" style="background:#3a3f47"></div></article>
  <article class="post"><div class="post-media" style="background:#3a3f47"></div></article>
  <article class="post"><div class="post-media" style="background:#3a3f47"></div></article>
</main>
<div class="feed-shade"></div>

<header class="site-header">
  <div class="brand"><span>Trondix</span><span class="brand-square"></span></div>
  <form class="search">
    <button class="search-button" type="button">SEARCH</button>
  </form>
  <nav class="main-nav">
    <a href="#" style="left:834px">Login</a>
    <a href="#" style="left:912px">How it works</a>
    <a href="#" style="left:1034px">Business</a>
  </nav>
</header>

<section class="login-panel">
  <span class="panel-tag">LOGIN</span>
  <div class="panel-brand"><span class="panel-brand-square"></span><span>Trondix</span></div>
  <a class="social-login"><span class="social-square"></span><span>Login with Linkora</span></a>
  <div class="divider">or</div>
  <h1 class="slogan">Shop Directly from your profile</h1>
  <div class="field field-username">Username</div>
  <div class="field field-password">Password</div>
  <button class="signup-button" type="button">Sign Up</button>
</section>

</body>
</html>
```